Drillvane Business Card Design Project

We need a business card design for a new company called "Drillvane Systems". Drillvane provides 3D visualization software for subsurface oil and gas data so you can make confident downhole decisions.

Our goal is to provide easy to understand big pictures of your data so your can make confident planning decisions.

Our tagline is
SEAMLESS DATA SHARING. EFFECTIVE COLLABORATION. CONFIDENT DECISION-MAKING

Check out http://www.drillvane-example.com for more ideas.

The design should promote a technology company that delivers web-based solutions focused on photo-realistic 3D graphics.

The colors from our existing logo (attached) are one option but not a requirement. The design SHOULD NOT use the existing logo.

The design should be two sided and full color. If you require any special print considerations (example: paper type, matte finish, metallic ink, etc) please provide detailed comments. Please also specify any desired details such as rounding of corners, etc.

IF YOU USE BLACK our printer states "We recommend using CMYK black (0, 0, 0, 100) or for a rich black (60, 40, 40, 100). Ensure your artwork is in CMYK mode before adjusting the black."

For design purposes you can use the following contact information

name: Marcus Pell
title: founder
phone: 555.987.6543
email: marcus@drillvane-example.com

company information
Drillvane is our "branded" name
"Drillvane Systems" is our official name
www.drillvane-example.com

address:
Suite 210
482 Larkin Avenue SW
Calgary, AB, Canada
T3K 4R8

Target Market(s)

Companies spend a lot of time collecting, organizing and analyzing data but it's really hard to to get a big picture view of current and planned projects, especially in context to existing wellbores, geology and downhole equipment

Drillvane enables you to explore the big picture in an immersive, 3D environment. Our goal is to help transform you rich data into an easily understood picture, to make confident planning decisions and anticipate trouble events before the expensive execution phase.

Industry/Entity Type

Oil And Gas

Requirements
Must have
• The business card design should be sized to a standard 3.5 x 2 inches and print ready. See the attachment for a sample sized card
It MUST meet these requirements:
Exported as PDF file with two pages:
page 1: front design
page 2: back design
All Images must be 300ppi or higher (at 100%)
CMYK colour mode
0.125 inches of bleed on all sides (0.25 inches additional width and height)
0.125 inch safety margin (inside trim line)

```html
<!DOCTYPE html>
<html lang="en">
<head>
<meta charset="utf-8">
<title>Drillvane Systems – Business Card</title>
<link rel="stylesheet" href="https://fonts.googleapis.com/css2?family=Roboto:wght@300;400;500&display=swap">
<style>
  :root {
    --stage: #58585a;
    --card-black: #000000;
    --brand-green: #8dc63f;
    --green-deep: #7bb534;
    --text-white: #ffffff;
    --text-soft: #e6e6e6;
  }
  * { margin: 0; padding: 0; box-sizing: border-box; }
  html, body {
    width: 1200px;
    height: 933px;
    overflow: hidden;
    background: var(--stage);
    font-family: "Roboto", Helvetica, Arial, sans-serif;
  }
  .stage { position: relative; width: 1200px; height: 933px; }

  .card {
    position: absolute;
    top: 315px;
    width: 474px;
    height: 270px;
    border-radius: 22px;
  }
  .card--front { left: 108px; background: var(--card-black); }
  .card--back  { left: 629px; background: var(--brand-green); }

  .front-brand {
    position: absolute;
    left: 58px;
    top: 140px;
    width: 124px;
    text-align: center;
    color: var(--brand-green);
    font-weight: 500;
    font-size: 21px;
    letter-spacing: -0.2px;
  }

  .contact {
    position: absolute;
    left: 212px;
    top: 43px;
    color: var(--text-soft);
    font-weight: 300;
    font-size: 14px;
    line-height: 18px;
  }
  .contact__name {
    color: var(--brand-green);
    font-size: 21px;
    line-height: 26px;
    font-weight: 300;
  }
  .contact__title {
    color: var(--text-white);
    font-size: 16.5px;
    line-height: 22px;
    margin-bottom: 8px;
  }
  .contact__lines { margin-bottom: 11px; }

  .back-brand {
    position: absolute;
    inset: 0;
    display: flex;
    align-items: center;
    justify-content: center;
    color: var(--green-deep);
    font-weight: 500;
    font-size: 66px;
    letter-spacing: -1px;
  }
</style>
</head>
<body>
<main class="stage">
  <section class="card card--front" aria-label="Business card front">
    <div class="front-brand">Drillvane</div>
    <div class="contact">
      <p class="contact__name">Marcus Pell</p>
      <p class="contact__title">founder</p>
      <div class="contact__lines">
        <p>phone: 555.987.6543</p>
        <p>email: marcus@drillvane-example.com</p>
      </div>
      <address style="font-style: normal;">
        <p>Suite 210</p>
        <p>482 Larkin Avenue SW</p>
        <p>Calgary, AB, Canada</p>
        <p>T3K 4R8</p>
        <p>www.drillvane-example.com</p>
      </address>
    </div>
  </section>

  <section class="card card--back" aria-label="Business card back">
    <div class="back-brand">Drillvane</div>
  </section>
</main>
</body>
</html>
```